Womens Personal Training studio needs new year flyers

I need a double sided A5 flyer to attract Women / Mothers to my fitness business, Blossom Daily, in the new year.

My business colour is teal, I am located in Springwood QLD Aus

Exclusive studio training for women. At Blossom Daily we don't make New years resolutions, we Empower you to make the changes for life!

examples of pain Q's: Do you feel guilty about wanting to do something for yourself? Do you worry about what exercises are safe post baby? Are you struggling to regain control of your body and your life?

Would you like to love yourself and your body as much as you lvoe your baby?

I work with women to apporpriately and progressivley rebuild their bodies post preganany. As the Leading specialist in Pre and Post Natal Rehabilitation and Fitness in Logan, Corinne knows what it takes to find the right balance. With a vision of Empowering this generation to inspire the next, Corinne teaches skills for LIFE so you can lead your family to a Healthier, Fitter and Stronger future! Using a fusion of Pilates, Strength Conditioning and Cardio Corinne customises a plan for each individual. Your free consultation is waiting call now and learn the first steps to making the change Valued at $147 Don’t Miss out!! Corinne 0438 270 614

Quote to go with image "Corinne doesn't just help you achieve your weight loss goals she works with you to make sure you are 'Blossom Daily'." Maren Holt July 2013

Target Market(s)

Women / Mothers

Industry/Entity Type

Training

Requirements
Must have
• call to action
contact details
Corinne Ashby
0438 270 614
corinne@blossomdailystudio.net.au
www.blossomdailystudio.net.au

```html
<!DOCTYPE html>
<html lang="en">
<head>
<meta charset="utf-8">
<title>Blossom Daily – New Year Flyer</title>
<link href="https://fonts.googleapis.com/css2?family=PT+Sans:ital,wght@0,400;0,700;1,400;1,700&display=swap" rel="stylesheet">
<style>
  :root {
    --teal: #138489;
    --teal-mid: #2a9c9f;
    --teal-dark: #1b6f73;
    --teal-text: #127f85;
    --ink: #3a4a4c;
    --white: #ffffff;
    --backdrop: #2c3133;
  }
  * { box-sizing: border-box; margin: 0; padding: 0; }
  html, body { width: 1200px; height: 957px; overflow: hidden; }
  body { background: var(--backdrop); font-family: "PT Sans", sans-serif; position: relative; }

  .page { position: absolute; top: 78px; width: 566px; height: 800px; background: var(--white); overflow: hidden; }
  .page--front { left: 20px; }
  .page--back { left: 614px; }

  /* Front */
  .wave { position: absolute; left: 0; top: 100px; width: 566px; height: 220px;
    background: linear-gradient(170deg, #ffffff 0%, #bff0f4 30%, #3fc3cf 55%, #8ee0e8 72%, #ffffff 100%); }
  .brand { position: absolute; left: 40px; top: 42px; display: flex; align-items: center; gap: 14px;
    color: var(--teal); font-size: 36px; font-weight: 400; }
  .brand__dot { width: 22px; height: 22px; border-radius: 50%; background: var(--teal); }
  .hero-photo { position: absolute; left: 256px; top: 215px; width: 310px; height: 405px;
    background: linear-gradient(180deg, #e9eceb 0%, #d7cfc7 45%, #b9c7a8 75%, #eef0ee 100%); }
  .questions { position: absolute; left: 34px; top: 340px; width: 240px; color: var(--ink); font-size: 19px; line-height: 1.2; }
  .questions p { margin-bottom: 12px; }
  .questions .questions__lead { font-weight: 700; font-size: 20px; width: 300px; }

  .front-band { position: absolute; left: 0; top: 628px; width: 566px; height: 122px; background: var(--teal-mid);
    color: var(--white); text-align: center; padding-top: 12px; }
  .front-band__headline { font-size: 31px; line-height: 1.1; }
  .front-band__tagline { font-size: 16px; line-height: 1.25; margin-top: 4px; }
  .front-band__contact { font-size: 17px; font-weight: 700; margin-top: 6px; }
  .front-strip { position: absolute; left: 0; top: 750px; width: 566px; height: 50px; background: var(--teal-dark);
    color: var(--white); font-size: 13.5px; display: flex; justify-content: space-around; align-items: center; }

  /* Back */
  .back-panel { position: absolute; left: 0; top: 0; width: 566px; height: 456px; background: var(--teal);
    color: var(--white); padding: 44px 28px 0 30px; font-size: 16.5px; line-height: 1.38; }
  .back-panel p { margin-bottom: 8px; }
  .price { font-size: 26px; }
  .cta { font-size: 28px; font-weight: 700; font-style: italic; line-height: 1.15; margin-top: 4px; }
  .cta-phone { font-size: 21px; }
  .results { position: absolute; left: 312px; top: 410px; width: 242px; height: 312px; background: var(--white);
    padding: 4px; display: flex; gap: 6px; }
  .results__shot { flex: 1; background: linear-gradient(180deg, #1c6f86 0%, #2a7c92 70%, #4b5356 100%); }
  .testimonial { position: absolute; left: 28px; top: 478px; width: 260px; color: var(--teal-text);
    font-weight: 700; font-style: italic; font-size: 22px; line-height: 1.32; }
  .testimonial__brand { font-size: 31px; line-height: 1.18; margin-top: 4px; }
  .testimonial__by { font-size: 16px; margin-top: 4px; }
  .back-band { position: absolute; left: 0; top: 735px; width: 566px; height: 65px; background: var(--teal);
    color: var(--white); text-align: center; padding-top: 9px; }
  .back-band__name { font-size: 19px; font-weight: 700; }
  .back-band__links { font-size: 14px; display: flex; justify-content: space-around; margin-top: 2px; }
</style>
</head>
<body>

<section class="page page--front">
  <div class="wave" role="img" aria-label="Flowing turquoise wave decoration with soft bubbles"></div>
  <div class="brand"><span class="brand__name">Blossom Daily</span><span class="brand__dot"></span></div>
  <div class="hero-photo" role="img" aria-label="Photo of a smiling mother in a headband holding her toddler drinking from a blue bottle"></div>
  <div class="questions">
    <p>Do you feel guilty about wanting to do something for yourself?</p>
    <p>Do you worry about what exercises are safe post baby?</p>
    <p>Are you struggling to regain control of your body and your life?</p>
    <p class="questions__lead">Would you like to love yourself and your body as much as you lvoe your baby?</p>
  </div>
  <div class="front-band">
    <div class="front-band__headline">Exclusive studio training for women</div>
    <div class="front-band__tagline">At Blossom Daily we don't make New years resolutions<br>we Empower you to make the changes for life!</div>
    <div class="front-band__contact">Corinne Ashby 0438 270 614</div>
  </div>
  <div class="front-strip">
    <span>corinne@blossomdailystudio.net.au</span>
    <span>www.blossomdailystudio.net.au</span>
  </div>
</section>

<section class="page page--back">
  <div class="back-panel">
    <p>I work with women to apporpriately and progressivley rebuild their bodies post preganany. As the Leading specialist in Pre and Post Natal Rehabilitation and Fitness in Logan, Corinne knows what it takes to find the right balance. With a vision of Empowering this generation to inspire the next, Corinne teaches skills for LIFE so you can lead your family to a Healthier, Fitter and Stronger future! Using a fusion of Pilates, Strength Conditioning and Cardio Corinne customises a plan for each individual.</p>
    <p>Your free consultation is waiting call now and learn the first steps to making the change Valued at <span class="price">$147</span></p>
    <div class="cta">Don’t Miss out!!</div>
    <div class="cta-phone">Corinne 0438 270 614</div>
  </div>
  <div class="results">
    <div class="results__shot" role="img" aria-label="Before photo: side view of a client in a pink top against a blue wall"></div>
    <div class="results__shot" role="img" aria-label="After photo: side view of the same client in a white top against a blue wall"></div>
  </div>
  <blockquote class="testimonial">
    Corinne doesn't just help you achieve your weight loss goals she works with you to make sure you are
    <div class="testimonial__brand">'Blossom Daily'."</div>
    <div class="testimonial__by">Maren Holt July 2013</div>
  </blockquote>
  <div class="back-band">
    <div class="back-band__name">Corinne Ashby 0438 270 614</div>
    <div class="back-band__links">
      <span>corinne@blossomdailystudio.net.au</span>
      <span>www.blossomdailystudio.net.au</span>
    </div>
  </div>
</section>

</body>
</html>
```